Banner for homepage

It is a new banner for the homepage, temporary site address is 203.0.113.57 ( is the biggest banner only ) . Would be 5 variations for image content as below (in Portuguese ) :

Image 1:
Leitor de codigo de barras
Todos os tipos de leitores de código de barras para as mais diversas aplicações.
( example of product images in : http://www.quorvelidx.com/en-US/Pages/Category.aspx?category=barcode-scanners&cat=QMT)

Image 2:
Impressora de etiquetas
Identifique o que for nessário com o melhor custo/beneficio e flexibilidade de materiais de impressão.
( example of product images in : tarnix.com in label printers desktop and industrial)

Image 3:
Impressora de cupom
Imprima recibos e cupons fiscais com agilidade e qualidade, temos a impressora certa para o seu PDV.
( example of product images in : http://www.plivorato.com.br/equipamento-categoria-impressoras+fiscais.html)

Image 4:
Coletor de dados
Computadores móveis com leitor de código de barras, que levam a automação para frente de trabalho.
( example of product images in : http://www.quorvelidx.com/en-US/Pages/Category.aspx?cat=QMT&category=hand-held-mobile-computer)

Image 5:
Etiquetas e Ribbons:
Etiquetas adesivas e não adesivas em vários de tipos de materiais, papéis e plásticos. O ribbon certo para impressão perfeita em cada material.
( example of product images in : http://www.lumetrask.com/cats/supplies/barcode-printer.htm?nav=hdr)

```html
<!DOCTYPE html>
<html lang="pt-BR">
<head>
<meta charset="utf-8">
<title>Travessa – Soluções em Automação e Código de barras</title>
<link rel="stylesheet" href="https://fonts.googleapis.com/css2?family=Oswald:wght@400;500&family=Jost:wght@400;500&family=Arimo:wght@400;700&display=swap">
<style>
  :root{
    --red:#c9353a;
    --page:#ececec;
    --nav-dark:#2a2a2a;
    --white:#ffffff;
    --ink:#3a3a3a;
    --hero-bg:#d5d6d7;
    --btn-red:#cc3338;
    --gold:#d2a668;
    --brown:#6e5a50;
  }
  *{box-sizing:border-box;margin:0;padding:0}
  html,body{width:1200px;height:588px;overflow:hidden}
  body{background:var(--page);font-family:"Arimo",Arial,sans-serif;position:relative}
  .site-header{position:absolute;left:0;top:0;width:1200px;height:107px;background:var(--red)}
  .brand{position:absolute;left:112px;top:16px;height:40px;display:flex;align-items:center;gap:10px}
  .brand-mark{width:22px;height:22px;background:var(--white)}
  .brand-name{font-family:"Arimo",Arial,sans-serif;font-weight:700;font-size:28px;color:var(--white)}
  .tagline{position:absolute;left:124px;top:61px;font-size:12.5px;color:var(--white)}
  .top-links{position:absolute;right:90px;top:11px;display:flex;font-size:12px;font-weight:700;color:var(--white)}
  .top-links span{padding:0 11px;border-left:1px solid rgba(255,255,255,.7)}
  .top-links span:first-child{border-left:none}
  .top-links span:last-child{padding-right:0}
  .contact-box{position:absolute;top:38px;height:47px;background:var(--white);padding:5px 11px;font-family:"Oswald",sans-serif}
  .contact-box .title{font-size:16px;color:#333;line-height:1.2}
  .contact-box .sub{font-size:11px;color:var(--red);line-height:1.4}
  .chat{left:838px;width:113px}
  .phones{left:967px;width:145px}
  .phones svg{position:absolute;right:10px;top:20px}
  .main-nav{position:absolute;left:82px;top:97px;width:1051px;height:43px;background:linear-gradient(#4a4a4a,var(--nav-dark));border-radius:3px;display:flex;align-items:center}
  .main-nav a{font-family:"Oswald",sans-serif;font-size:13px;color:var(--white);text-decoration:none;padding:0 11px;height:43px;line-height:43px;border-right:1px solid #555}
  .main-nav a:first-child{padding-left:21px}
  .search{position:absolute;right:10px;top:8px;width:152px;height:27px;background:#2b2b2b;border:1px solid #1c1c1c;border-radius:3px;font-size:12px;color:#bbb;padding:6px 7px}
  .search svg{position:absolute;right:7px;top:7px}
  .hero{position:absolute;left:103px;top:161px;width:751px;height:341px;background:linear-gradient(#dcdddd,var(--hero-bg));border-radius:7px;overflow:hidden}
  .hero h1{position:absolute;left:45px;top:30px;font-family:"Jost",sans-serif;font-weight:500;font-size:35px;line-height:40px;color:var(--red);letter-spacing:.5px}
  .hero p{position:absolute;left:47px;top:122px;width:278px;font-family:"Jost",sans-serif;font-size:19px;line-height:21px;color:var(--ink)}
  .hero .cta{position:absolute;left:44px;top:214px;width:152px;height:52px;border:3px solid var(--white);border-radius:26px;background:var(--btn-red);color:var(--white);font-family:"Jost",sans-serif;font-size:19px;display:flex;align-items:center;justify-content:center;box-shadow:0 1px 3px rgba(0,0,0,.25)}
  .hero .product{position:absolute;left:420px;top:22px;width:300px;height:319px;border-radius:40px 40px 0 0;background:linear-gradient(160deg,#3d3d3d 0%,#d8382f 45%,#2e2e2e 100%)}
  .promo{position:absolute;left:878px;width:237px;height:163px;border-radius:4px;overflow:hidden}
  .promo h2{position:absolute;left:24px;top:16px;font-family:"Oswald",sans-serif;font-weight:500;font-size:33px;line-height:38px;white-space:nowrap}
  .promo p{position:absolute;left:24px;top:70px;font-size:12px;line-height:16px;color:var(--white)}
  .promo .more{position:absolute;left:24px;top:116px;width:94px;height:24px;border-radius:12px;font-family:"Oswald",sans-serif;font-size:13px;color:var(--white);display:flex;align-items:center;justify-content:center}
  .promo .art{position:absolute}
  .fast{top:162px;background:linear-gradient(#3a3836,#1e1d1c)}
  .fast h2 .a{color:var(--gold)}
  .fast h2 .b{color:var(--white)}
  .fast .more{background:linear-gradient(#e2c593,#b98d55)}
  .fast .art{left:142px;top:80px;width:84px;height:72px;background:linear-gradient(#c98a4a,#8a5626)}
  .billing{top:340px;background:linear-gradient(#8a7a72,var(--brown))}
  .billing h2 .a{color:#3b302b}
  .billing h2 .b{color:var(--white)}
  .billing .more{background:linear-gradient(#e24a3f,#b1221c)}
  .billing .art{left:138px;top:70px;width:86px;height:80px;background:linear-gradient(#1e3b40,#0f1d20)}
  .section-title{position:absolute;left:114px;top:536px;font-family:"Oswald",sans-serif;font-weight:500;font-size:19px;color:#444}
  .section-band{position:absolute;left:103px;top:572px;width:1030px;height:20px;background:#e1e1e1}
</style>
</head>
<body>
  <header class="site-header">
    <div class="brand"><span class="brand-mark"></span><span class="brand-name">Travessa</span></div>
    <div class="tagline">Soluções em Automação e Código de barras</div>
    <nav class="top-links"><span>Principal</span><span>Quem Somos</span><span>Entre em Contato</span></nav>
    <div class="contact-box chat"><div class="title">CHAT ONLINE</div><div class="sub">CLIQUE AQUI</div></div>
    <div class="contact-box phones"><div class="title">TELEFONES</div><div class="sub">TODOS OS ESTADOS</div>
      <svg width="9" height="6" viewBox="0 0 9 6"><path d="M0 0h9L4.5 6z" fill="#555"/></svg></div>
  </header>

  <nav class="main-nav">
    <a>LEITOR DE CÓDIGO DE BARRAS</a><a>IMPRESSORA DE ETIQUETAS</a><a>AUTOMAÇÃO COMERCIAL</a><a>ETIQUETAS</a><a>COLETOR DE DADOS</a><a>IMPRESSORA DE CARTÃO</a><a>MARCAS</a>
    <div class="search">Busca
      <svg width="12" height="12" viewBox="0 0 12 12"><circle cx="5" cy="5" r="3.6" fill="none" stroke="#ddd" stroke-width="1.6"/><path d="M7.6 7.6L11 11" stroke="#ddd" stroke-width="2"/></svg></div>
  </nav>

  <section class="hero">
    <h1>LEITOR DE CODIGO<br>DE BARRAS</h1>
    <p>Todos os tipos de leitores de código de barras para as mais diversas aplicações</p>
    <div class="cta">Veja Mais</div>
    <div class="product" role="img" aria-label="Foto de leitor de código de barras de mão, vermelho e preto"></div>
  </section>

  <aside class="promo fast">
    <h2><span class="a">Entrega</span><span class="b">Rápida</span></h2>
    <p>Enviamos sua compra<br>para todo o Brasil.</p>
    <div class="more">Leia Mais</div>
    <div class="art" role="img" aria-label="Ilustração de caixa de papelão para entrega"></div>
  </aside>

  <aside class="promo billing">
    <h2><span class="a">Boleto</span><span class="b">Faturado</span></h2>
    <p>Receba seu pedido<br>com os boletos.</p>
    <div class="more">Leia Mais</div>
    <div class="art" role="img" aria-label="Ilustração de sacola de compras"></div>
  </aside>

  <h3 class="section-title">DESTAQUES</h3>
  <div class="section-band"></div>
</body>
</html>
```